Ad Banner for knowledge management portal - Benefit of Knowledge Management

This banner is used in a knowledge management web portal.
1. Banner size: 940x380
2. Business background: Provides maintenance, design and engineering, construction, machinery operation, material procurement and production management services for petrochemical and refinery business
3. We would like to see designs that promote the benefit of knowledge managment. "Knowledge of each individuals can be connected to build a greater benefit to the organization"
4. Key message in the banner:
- Knowledge
- Connected
- Team

• Do not include picture of real people in the banner

```html
<!DOCTYPE html>
<html lang="en">
<head>
<meta charset="utf-8">
<title>Benefit of Knowledge Management</title>
<link href="https://fonts.googleapis.com/css2?family=Arimo:wght@400;700&family=Gochi+Hand&display=swap" rel="stylesheet">
<style>
  :root {
    --navy-deep: #07193d;
    --navy: #143c78;
    --blue-mid: #2f6fb4;
    --blue-light: #8fd0ee;
    --cyan-pale: #d9f3fb;
    --white: #ffffff;
    --ink: #0a0a0a;
    --chalk: #ffffff;
    --button-top: #2a7fe0;
    --button-bottom: #0a49b5;
    --bubble: #2a86d8;
  }
  html, body {
    margin: 0;
    padding: 0;
    overflow: hidden;
    background: var(--white);
  }
  .banner {
    position: relative;
    width: 1200px;
    height: 485px;
    overflow: hidden;
    font-family: "Arimo", Arial, sans-serif;
  }
  .backdrop {
    position: absolute;
    inset: 0;
    background:
      radial-gradient(ellipse 60% 30% at 30% 100%, rgba(0,0,0,0.9) 0%, rgba(0,0,0,0.55) 55%, rgba(0,0,0,0) 100%),
      linear-gradient(180deg, rgba(0,0,0,0) 70%, rgba(0,0,0,0.45) 100%),
      linear-gradient(100deg, var(--navy-deep) 0%, var(--navy) 30%, var(--blue-mid) 52%, var(--blue-light) 64%, var(--cyan-pale) 74%, var(--white) 82%, var(--cyan-pale) 100%);
  }
  .headline {
    position: absolute;
    left: 453px;
    top: 44px;
    margin: 0;
    font-weight: 400;
    font-size: 42px;
    line-height: 59px;
    letter-spacing: 0.6px;
    color: var(--ink);
    white-space: nowrap;
  }
  .note {
    position: absolute;
    margin: 0;
    font-family: "Gochi Hand", cursive;
    color: var(--chalk);
    white-space: nowrap;
  }
  .idea-bubble {
    position: absolute;
    left: 60px;
    top: 64px;
    width: 132px;
    height: 116px;
  }
  .idea-bubble .note {
    left: 14px;
    top: 46px;
    font-size: 19px;
    line-height: 24px;
  }
  .bulb-art {
    position: absolute;
    left: 396px;
    top: 226px;
    width: 120px;
    height: 110px;
    border-radius: 50%;
    background: radial-gradient(ellipse at 50% 45%, rgba(220,240,255,0.85) 0%, rgba(110,180,250,0.55) 35%, rgba(60,130,220,0.2) 60%, rgba(60,130,220,0) 72%);
  }
  .solution-note {
    left: 539px;
    top: 254px;
    font-size: 22px;
    line-height: 38px;
  }
  .handshake-art {
    position: absolute;
    left: 740px;
    top: 252px;
    width: 196px;
    height: 110px;
    border-radius: 50%;
    background: radial-gradient(ellipse at 50% 50%, rgba(40,140,220,0.75) 0%, rgba(70,160,230,0.45) 40%, rgba(120,190,240,0.15) 62%, rgba(120,190,240,0) 72%);
  }
  .team-note {
    left: 862px;
    top: 342px;
    font-size: 21px;
    line-height: 37px;
    color: var(--ink);
  }
  .team-note span { display: block; }
  .team-note .indent { padding-left: 26px; }
  .learn-button {
    position: absolute;
    left: 26px;
    top: 370px;
    width: 549px;
    height: 77px;
    box-sizing: border-box;
    border: 4px solid var(--white);
    background: var(--white);
    padding: 4px;
    text-decoration: none;
  }
  .learn-button .face {
    display: flex;
    align-items: center;
    justify-content: center;
    height: 100%;
    border: 2px solid var(--navy-deep);
    box-sizing: border-box;
    background: linear-gradient(180deg, var(--button-top), var(--button-bottom));
    color: var(--white);
    font-size: 23px;
    white-space: nowrap;
  }
  .learn-button strong { font-weight: 700; margin-left: 6px; }
</style>
</head>
<body>
  <div class="banner">
    <div class="backdrop" role="img" aria-label="Refinery towers at dusk in deep blue on the left, fading into a pale blueprint of a floor plan with a white perspective grid on the right"></div>

    <p class="headline">Knowledge of each individuals<br>can be connected to build a greater<br>benefit to the organization</p>

    <div class="idea-bubble">
      <svg width="132" height="116" viewBox="0 0 132 116" aria-hidden="true">
        <path d="M34 92 L20 112 L52 96 Z" fill="var(--bubble)" stroke="var(--white)" stroke-width="3" stroke-linejoin="round"/>
        <ellipse cx="68" cy="56" rx="62" ry="46" fill="var(--bubble)" stroke="var(--white)" stroke-width="3"/>
        <path d="M30 88 L50 94" stroke="var(--bubble)" stroke-width="5"/>
      </svg>
      <p class="note">Better idea</p>
    </div>

    <div class="bulb-art" role="img" aria-label="Sketched glowing light bulb"></div>
    <p class="note solution-note">Better<br>Solution</p>

    <div class="handshake-art" role="img" aria-label="Sketched blue handshake"></div>
    <p class="note team-note"><span>Knowledge</span><span>Connected</span><span class="indent">Team</span></p>

    <a class="learn-button" href="#lesson-learned"><span class="face">Click here to learn more about <strong>Lesson Learned</strong></span></a>
  </div>
</body>
</html>
```